New Album "A night beside the silver hills"

I need a cd cover for a new pop rock album called "A night beside the silver hills"
The main color of the artwork shall obviously be orange. The artwork shouldn't be too "obvious", but it would be better something a bit abstract.
Please remember that it is a Music Cd Cover, so do not send business logo or advertisement images.

Target Market(s)

It's a pop rock album, so the target customers are young and adult people from 15-60 years old

Requirements
Must have
• Orange as main colour
The Artist name is: Remy Castellan
The Title: A night beside the silver hills
Should not have
• Not too cheesy or dreamy images please. No simple sunset or sunrise pics

```html
<!DOCTYPE html>
<html lang="en">
<head>
<meta charset="utf-8">
<title>A Night Beside the Silver Hills – Remy Castellan</title>
<link rel="stylesheet" href="https://fonts.googleapis.com/css2?family=Poppins:wght@500;600;700&display=swap">
<style>
  :root {
    --backdrop: #f6a21a;
    --orange-deep: #f0501e;
    --orange-mid: #f7821c;
    --orange-bright: #ffa31f;
    --yellow: #ffd21a;
    --cream: #fff3df;
    --slate: #7d7b78;
    --white: #ffffff;
    --title-accent: #f7901e;
  }

  * { box-sizing: border-box; margin: 0; padding: 0; }

  html, body {
    width: 1200px;
    height: 800px;
    overflow: hidden;
  }

  body {
    background: var(--backdrop);
    font-family: "Poppins", sans-serif;
    position: relative;
  }

  .album-cover {
    position: absolute;
    left: 280px;
    top: 80px;
    width: 640px;
    height: 640px;
    overflow: hidden;
  }

  .cover-art {
    position: absolute;
    inset: 0;
    background:
      radial-gradient(circle at 30% 75%, var(--slate) 0 18%, transparent 34%),
      radial-gradient(ellipse at 80% 20%, var(--cream) 0%, transparent 30%),
      radial-gradient(ellipse at 20% 45%, var(--yellow) 0%, transparent 28%),
      radial-gradient(ellipse at 85% 70%, var(--yellow) 0%, transparent 30%),
      radial-gradient(ellipse at 10% 90%, var(--orange-deep) 0%, transparent 35%),
      radial-gradient(ellipse at 60% 10%, var(--orange-deep) 0%, transparent 30%),
      linear-gradient(135deg, var(--orange-bright) 0%, var(--orange-mid) 50%, var(--orange-deep) 100%);
  }

  .album-title {
    position: absolute;
    left: 196px;
    top: 440px;
    color: var(--white);
    text-transform: uppercase;
    line-height: 1;
    font-weight: 700;
  }

  .album-title span { display: block; }

  .album-title .title-intro {
    font-weight: 600;
    font-size: 36px;
    text-align: right;
    margin-bottom: 4px;
  }

  .album-title .title-line {
    font-size: 54px;
    letter-spacing: 0.5px;
  }

  .album-title .title-accent { color: var(--title-accent); }

  .artist-name {
    position: absolute;
    right: 22px;
    top: 120px;
    writing-mode: vertical-rl;
    color: var(--white);
    font-weight: 600;
    font-size: 30px;
    letter-spacing: 2px;
    text-transform: uppercase;
  }
</style>
</head>
<body>
  <main class="album-cover">
    <div class="cover-art" role="img" aria-label="Abstract artwork of overlapping flowing petal shapes in orange, red, yellow, white and grey"></div>
    <h1 class="album-title">
      <span class="title-intro">A night</span>
      <span class="title-line">Beside the</span>
      <span class="title-line title-accent">Silver</span>
      <span class="title-line">Hills</span>
    </h1>
    <p class="artist-name">Remy Castellan</p>
  </main>
</body>
</html>
```